Info flyer to showcase security camera install and remote video monitoring.

I am looking for an attractive looking flyer that is simple and has some text content and some photos to show prospective clients what services I can provide them.

The two main services that I want to showcase are:
1. Security Camera & NVR Installations and maintenance
2. Remote Video Monitoring for business. This can be a temporary service or ongoing/long term.

Target Market(s)

Construction, Retail, Industrial, Commercial

Industry/Entity Type

Security

Font styles to use
Serif

Colors

Designer to choose colors to be used in the design.

```html
<!DOCTYPE html>
<html lang="en">
<head>
<meta charset="utf-8">
<title>Vantage Secure Systems – Security Flyer</title>
<link rel="stylesheet" href="https://fonts.googleapis.com/css2?family=Lato:wght@400;700;900&family=Oswald:wght@400;500&display=swap">
<style>
  :root {
    --gold: #c9a02a;
    --charcoal: #3a3a3c;
    --ink: #4a4a4c;
    --body: #5a5a5a;
    --paper: #ffffff;
    --mist: #e9ebee;
    --footer: #3b3b3d;
  }
  * { margin: 0; padding: 0; box-sizing: border-box; }
  html, body { width: 762px; height: 1200px; overflow: hidden; background: var(--paper); }
  .flyer {
    position: relative; width: 762px; height: 1200px; overflow: hidden;
    background: linear-gradient(180deg, #ffffff 45%, #f1f2f3 75%, #e4e5e7 100%);
    font-family: 'Lato', sans-serif; color: var(--body);
  }
  .hero-backdrop {
    position: absolute; left: 0; top: 0; width: 762px; height: 470px;
    background: linear-gradient(180deg, #dfe3e8 0%, #f3f5f7 40%, #e6e9ed 75%, #d9dde2 100%);
  }
  .hero-camera {
    position: absolute; left: 410px; top: 10px; width: 352px; height: 440px;
    border-radius: 46% 0 40% 48%;
    background: radial-gradient(ellipse at 45% 70%, #3b3d42 0%, #5c5f64 22%, #d9d6cd 45%, #ecebe5 70%, rgba(236,235,229,0) 100%);
  }
  .brand {
    position: absolute; left: 42px; top: 104px;
    display: flex; align-items: center; gap: 12px;
  }
  .brand-dot { width: 46px; height: 46px; border-radius: 50%; background: var(--gold); }
  .brand-name {
    font-family: 'Lato', sans-serif; font-weight: 900; color: var(--charcoal);
    font-size: 34px; line-height: 1.05; letter-spacing: 0.5px;
  }
  .wave { position: absolute; left: 0; top: 360px; width: 762px; height: 230px; }
  .photo-circle {
    position: absolute; left: 44px; width: 190px; height: 190px; border-radius: 50%;
    border: 7px solid #ffffff; box-shadow: -8px 0 0 var(--charcoal);
  }
  .photo-circle.first { top: 570px; background: radial-gradient(circle at 40% 45%, #d8d9db 0%, #a9abae 45%, #eceded 100%); }
  .photo-circle.second { top: 820px; background: radial-gradient(circle at 45% 55%, #f2f2f2 0%, #c4c6c9 40%, #ecedee 100%); }
  .content { position: absolute; left: 278px; top: 572px; width: 450px; }
  .headline {
    font-family: 'Oswald', sans-serif; font-weight: 500; color: var(--ink);
    font-size: 78px; line-height: 1; letter-spacing: 0.5px;
  }
  .tagline {
    font-weight: 700; color: var(--gold); font-size: 15px; text-transform: uppercase;
    margin-top: 8px; letter-spacing: 0.2px;
  }
  .pill {
    display: inline-block; background: var(--gold); color: #fff; font-weight: 900;
    font-size: 15px; text-transform: uppercase; padding: 5px 14px; border-radius: 14px;
  }
  .services { margin-top: 26px; }
  .services .pill { width: 276px; }
  .service-list { list-style: none; margin-top: 12px; }
  .service-list li {
    position: relative; padding-left: 22px; font-size: 17px; color: #444;
    line-height: 1.3; margin-bottom: 8px; text-align: justify;
  }
  .service-list li svg { position: absolute; left: 0; top: 4px; }
  .section { margin-top: 14px; }
  .section p { font-size: 12.6px; line-height: 1.45; margin-top: 8px; text-align: justify; }
  .footer {
    position: absolute; left: 0; bottom: 0; width: 762px; height: 60px; background: var(--footer);
    display: flex; align-items: center; justify-content: space-around; padding: 0 40px;
    color: #fff; font-size: 14px;
  }
  .footer span { display: flex; align-items: center; gap: 8px; }
</style>
</head>
<body>
<main class="flyer">
  <div class="hero-backdrop" role="img" aria-label="Softly blurred bright office interior background"></div>
  <div class="hero-camera" role="img" aria-label="Ceiling-mounted dome security camera"></div>

  <div class="brand">
    <div class="brand-dot"></div>
    <div class="brand-name">VANTAGE<br>SECURE SYSTEMS</div>
  </div>

  <svg class="wave" viewBox="0 0 762 230" preserveAspectRatio="none" aria-hidden="true">
    <path d="M0 30 C180 -10 330 90 520 70 C620 60 700 30 762 20 L762 50 C690 70 610 95 510 105 C330 120 180 40 0 70 Z" fill="var(--gold)"/>
    <path d="M0 70 C180 40 330 120 510 105 C610 95 690 70 762 50 L762 95 C640 110 520 130 380 150 C220 170 90 190 0 230 Z" fill="var(--charcoal)"/>
    <path d="M0 230 C90 190 220 170 380 150 C520 130 640 110 762 95 L762 105 C640 125 520 145 390 165 C230 185 100 205 10 230 Z" fill="#ffffff"/>
    <path d="M10 230 C100 205 230 185 390 165 C520 145 640 125 762 105 L762 230 Z" fill="#ffffff"/>
  </svg>

  <div class="photo-circle first" role="img" aria-label="Bullet security cameras mounted on a pole"></div>
  <div class="photo-circle second" role="img" aria-label="White dome camera on a wall bracket"></div>

  <section class="content">
    <h1 class="headline">LOREM IPSUM</h1>
    <p class="tagline">Simply dummy textof the printing and typesetting</p>

    <div class="services">
      <span class="pill">Services that we provided</span>
      <ul class="service-list">
        <li><svg width="14" height="12" viewBox="0 0 14 12"><path d="M1 6 L5 10 L13 1" fill="none" stroke="var(--gold)" stroke-width="2.4"/></svg>Security Camera &amp; NVR Installations and maintenance</li>
        <li><svg width="14" height="12" viewBox="0 0 14 12"><path d="M1 6 L5 10 L13 1" fill="none" stroke="var(--gold)" stroke-width="2.4"/></svg>Remote Video Monitoring for business. This can be a temporary service or ongoing/long term.</li>
      </ul>
    </div>

    <div class="section">
      <span class="pill">About us</span>
      <p>Lorem Ipsum is simply dummy text of the printing and typesetting industry. Lorem Ipsum has been the industry's standard dummy text ever since the 1500s, when an unknown printer took a galley of type and scrambled it to make a type specimen book. It has survived not only five centuries, but also the leap into electronic typesetting, remaining essentially un-</p>
    </div>

    <div class="section">
      <span class="pill">Why choose us</span>
      <p>Lorem Ipsum is simply dummy text of the printing and typesetting industry. Lorem Ipsum has been the industry's standard dummy text ever since the 1500s, when an unknown printer took a galley of type and scrambled it to make a type specimen book.</p>
    </div>
  </section>

  <footer class="footer">
    <span><svg width="14" height="14" viewBox="0 0 24 24"><path d="M6.6 10.8a15 15 0 0 0 6.6 6.6l2.2-2.2c.3-.3.7-.4 1-.2 1.1.4 2.3.6 3.6.6.6 0 1 .4 1 1V20c0 .6-.4 1-1 1A17 17 0 0 1 3 4c0-.6.4-1 1-1h3.5c.6 0 1 .4 1 1 0 1.3.2 2.5.6 3.6.1.3 0 .7-.2 1z" fill="#fff"/></svg>00000000000</span>
    <span><svg width="14" height="14" viewBox="0 0 24 24"><circle cx="12" cy="12" r="10" fill="none" stroke="#fff" stroke-width="2"/><path d="M2 12h20M12 2c3 3 3 17 0 20M12 2c-3 3-3 17 0 20" fill="none" stroke="#fff" stroke-width="1.6"/></svg>Lorem Ipsum is simply dummy text</span>
    <span><svg width="14" height="14" viewBox="0 0 24 24"><rect x="2" y="5" width="20" height="14" rx="2" fill="#fff"/><path d="M3 6l9 7 9-7" fill="none" stroke="var(--footer)" stroke-width="1.8"/></svg>Lorem Ipsum is simply dummy</span>
  </footer>
</main>
</body>
</html>
```